Filmproduktion braucht Visitenkarten und Briefpapier
Zielgruppe
Wir sind eine junge Filmproduktion Firma mit dem Namen Lichtkante.
Unser Kerngeschäft sind Image und Unternehmensfilme, sowie Event und Messefilme.
Aufgabenstellung
Wir sind junge, kreative, Filmschaffende und das soll sich auch in der Visitenkarte widerspiegeln, dennoch macht bitte auch ein paar klassische Vorschläge, manchmal ist weniger mehr.
Unser altes Briefpapier ist angehängt. Das neue Briefpapier muss von uns veränderbar sein, da wir noch nicht alle Daten haben wie Steuernummer und USt-ID, bitte aber schon als Dummy anlegen.
Unsere alten Visitenkarten sind angehängt, diese Daten Stimmen, aber ansonsten stimmt daran nix, wie wir finden. Bitte nicht daran Orientieren!!!
Bitte bei der Adresse Lichtkante GbR schreiben.
Unser neues Logo, jetzt in blau ist ebenfalls angehängt.
Viel Spass beim Designen.

```html
<!DOCTYPE html>
<html lang="de">
<head>
<meta charset="utf-8">
<title>Lichtkante – Geschäftsausstattung</title>
<link rel="stylesheet" href="https://fonts.googleapis.com/css2?family=Source+Sans+3:wght@400;600;700&display=swap">
<style>
  :root {
    --stage: #dcdcdc;
    --paper: #ffffff;
    --folder: #ececec;
    --ink: #1b1b1b;
    --muted: #5a5a5a;
    --blue: #4a90d0;
  }
  * { box-sizing: border-box; margin: 0; padding: 0; }
  html, body { width: 1200px; height: 912px; overflow: hidden; }
  body {
    position: relative;
    background: var(--stage);
    font-family: "Source Sans 3", sans-serif;
    color: var(--ink);
  }
  .sheet { position: absolute; background: var(--paper); overflow: hidden; }
  .wordmark {
    position: absolute;
    font-weight: 400;
    color: var(--ink);
    text-transform: uppercase;
    white-space: nowrap;
  }
  .nowrap { white-space: nowrap; }
  .blue { color: var(--blue); }

  /* Folder */
  .folder { left: 17px; top: 124px; width: 317px; height: 577px; background: var(--folder); }
  .folder .wordmark { left: 96px; top: 328px; font-size: 19px; letter-spacing: 13.4px; }

  /* Letterhead */
  .letter { left: 334px; top: 94px; width: 449px; height: 631px; }
  .letter-next { left: 783px; top: 136px; width: 400px; height: 577px; }
  .fold-mark { position: absolute; height: 1px; width: 11px; background: var(--blue); }
  .letter .fold-mark { left: 0; }
  .letter-next .fold-mark { left: 0; width: 4px; }

  .sender-line { position: absolute; font-size: 5.6px; white-space: nowrap; }
  .sender-line .sep { color: var(--blue); }
  .recipient { position: absolute; font-size: 8.4px; line-height: 10.9px; }
  .subject-row { position: absolute; display: flex; justify-content: space-between; font-size: 8.4px; }
  .subject { font-weight: 700; }
  .body-copy { position: absolute; font-size: 8.5px; line-height: 10.9px; white-space: nowrap; }
  .body-copy p + p { margin-top: 10.9px; }

  .footer { position: absolute; font-size: 7.7px; line-height: 9.8px; color: var(--muted); }
  .footer .col { position: absolute; top: 0; white-space: nowrap; }
  .footer h4 { color: var(--blue); font-weight: 700; font-size: inherit; }
  .bullet-list { list-style: none; }
  .bullet-list li { position: relative; padding-left: 11px; }
  .bullet-list li::before {
    content: ""; position: absolute; left: 0; top: 50%; transform: translateY(-50%);
    border-left: 5px solid var(--blue); border-top: 3px solid transparent; border-bottom: 3px solid transparent;
  }
  .bank { display: grid; grid-template-columns: 28px auto; }

  .letter .wordmark { left: 288px; top: 115px; font-size: 10px; letter-spacing: 6.9px; }
  .letter-next .wordmark { left: 253px; top: 105px; font-size: 9px; letter-spacing: 6.1px; }
  .letter-next .footer { font-size: 7px; line-height: 9.1px; }
  .letter-next .bank { grid-template-columns: 26px auto; }

  /* Business cards */
  .card { position: absolute; top: 725px; height: 141px; background: var(--paper); overflow: hidden; }
  .card .edge { position: absolute; left: 0; top: 0; bottom: 0; width: 8px; background: var(--blue); }
  .card .name { position: absolute; left: 85px; top: 18px; font-size: 11.2px; font-weight: 700; color: var(--blue); white-space: nowrap; }
  .card .address { position: absolute; left: 85px; top: 54px; font-size: 7.6px; line-height: 9.8px; white-space: nowrap; }
  .card .address .sep { color: var(--blue); }
  .card .contact { position: absolute; left: 85px; top: 93px; font-size: 7.6px; line-height: 9.8px; white-space: nowrap; }
  .card-front { left: 800px; width: 206px; background: var(--folder); }
  .card-front .wordmark { left: 26px; top: 97px; font-size: 11.5px; letter-spacing: 8.6px; }
</style>
</head>
<body>

  <section class="sheet folder" aria-label="Mappe">
    <div class="wordmark">Lichtkante</div>
  </section>

  <section class="sheet letter" aria-label="Briefbogen Seite 1">
    <span class="fold-mark" style="top:186px"></span>
    <span class="fold-mark" style="top:318px"></span>
    <span class="fold-mark" style="top:411px"></span>

    <div class="sender-line" style="left:67px; top:58px">Lichtkante GbR <span class="sep">|</span> Uferweg 12 <span class="sep">|</span> 12043 Berlin</div>
    <div class="recipient" style="left:64px; top:70px">Lichtkante GbR<br>Filmproduktion<br>Uferweg 12<br>12043 Berlin</div>
    <div class="wordmark">Lichtkante</div>

    <div class="subject-row" style="left:54px; top:170px; width:351px">
      <span class="subject">Filmproduktion braucht Visitenkarten und Briefpapier</span>
      <span><span class="blue">Leipzig</span>, 17. Oktober 2013</span>
    </div>

    <div class="body-copy" style="left:54px; top:192px">
      <p>Wir sind eine junge Filmproduktion Firma mit dem Namen Lichtkante. Unser Kerngeschäft<br>sind Image und Unternehmensfilme, sowie Event und Messefilme.</p>
      <p>Wir sind junge, kreative, Filmschaffende und das soll sich auch in der Visitenkarte widerspie-<br>geln, dennoch macht bitte auch ein paar klassische Vorschläge, manchmal ist weniger mehr.<br>Unser altes Briefpapier ist angehängt. Das neue Briefpapier muss von uns veränderbar sein, da<br>wir noch nicht alle Daten haben wie Steuernummer und USt-ID, bitte aber schon als Dummy<br>anlegen.<br>Unsere alten Visitenkarten sind angehängt, diese Daten Stimmen, aber ansonsten stimmt<br>daran nix, wie wir finden. Bitte nicht daran Orientieren!!! Bitte bei der Adresse Lichtkante GbR<br>schreiben. Unser neues Logo, jetzt in blau ist ebenfalls angehängt. Viel Spass beim Designen.</p>
      <p>Mit freundlichen Grüßen</p>
      <p>Fenja</p>
    </div>

    <div class="footer" style="left:54px; top:534px">
      <div class="col" style="left:0"><h4>Lichtkante GbR</h4>Filmproduktion<br>Uferweg 12<br>12043 Berlin</div>
      <div class="col" style="left:82px"><h4>Geschäftsführer:</h4>Malte Rieger<br>Jonas Berger<br>Lukas Hansen</div>
      <div class="col" style="left:170px"><h4>Ansprechpartner:</h4>Jonas Berger
        <ul class="bullet-list"><li>(01 70) 5 28 41 06</li><li>berger@lichtkante.example</li><li>www.lichtkante.example</li></ul></div>
      <div class="col" style="left:273px"><h4>Bankverbindung:</h4>Stadtbank Mitte
        <div class="bank"><span>BLZ:</span><span>200 300 40</span><span>Kto.:</span><span>480 615 273</span><span>St.-Nr.:</span><span>987/654/32100</span></div></div>
    </div>
  </section>

  <section class="sheet letter-next" aria-label="Briefbogen Folgeseite">
    <span class="fold-mark" style="top:169px"></span>
    <span class="fold-mark" style="top:285px"></span>
    <span class="fold-mark" style="top:372px"></span>

    <div class="sender-line" style="left:52px; top:53px; font-size:5px">Lichtkante GbR <span class="sep">|</span> Uferweg 12 <span class="sep">|</span> 12043 Berlin</div>
    <div class="recipient" style="left:50px; top:63px; font-size:7.6px; line-height:9.8px">Lichtkante GbR<br>Filmproduktion<br>Uferweg 12<br>12043 Berlin</div>
    <div class="wordmark">Lichtkante</div>

    <div class="subject-row" style="left:40px; top:154px; width:320px; font-size:7.6px">
      <span class="subject">Filmproduktion braucht Visitenkarten und Briefpapier</span>
      <span><span class="blue">Leipzig</span>, 17. Oktober 2013</span>
    </div>

    <div class="footer" style="left:40px; top:486px">
      <div class="col" style="left:0"><h4>Lichtkante GbR</h4>Filmproduktion<br>Uferweg 12<br>12043 Berlin</div>
      <div class="col" style="left:75px"><h4>Geschäftsführer:</h4>Malte Rieger<br>Jonas Berger<br>Lukas Hansen</div>
      <div class="col" style="left:154px"><h4>Ansprechpartner:</h4>Jonas Berger
        <ul class="bullet-list"><li>(01 70) 5 28 41 06</li><li>berger@lichtkante.example</li><li>www.lichtkante.example</li></ul></div>
      <div class="col" style="left:247px"><h4>Bankverbindung:</h4>Stadtbank Mitte
        <div class="bank"><span>BLZ:</span><span>200 300 40</span><span>Kto.:</span><span>480 615 273</span><span>St.-Nr.:</span><span>987/654/32100</span></div></div>
    </div>
  </section>

  <article class="card" style="left:174px; width:217px" aria-label="Visitenkarte Jonas Berger">
    <span class="edge"></span>
    <div class="name">Jonas Berger</div>
    <div class="address">Lichtkante GbR <span class="sep">|</span> Filmproduktion<br>Uferweg 12<br>12043 Berlin</div>
    <ul class="contact bullet-list"><li>(01 70) 5 28 41 06</li><li>berger@lichtkante.example</li><li>www.lichtkante.example</li></ul>
  </article>

  <article class="card" style="left:391px; width:204px" aria-label="Visitenkarte Lukas Hansen">
    <span class="edge"></span>
    <div class="name" style="left:72px">Lukas Hansen</div>
    <div class="address" style="left:72px">Lichtkante GbR <span class="sep">|</span> Filmproduktion<br>Uferweg 12<br>12043 Berlin</div>
    <ul class="contact bullet-list" style="left:72px"><li>(01 51) 62 37 14 85</li><li>hansen@lichtkante.example</li><li>www.lichtkante.example</li></ul>
  </article>

  <article class="card" style="left:595px; width:205px" aria-label="Visitenkarte Malte Rieger">
    <span class="edge"></span>
    <div class="name" style="left:72px">Malte Rieger</div>
    <div class="address" style="left:72px">Lichtkante GbR <span class="sep">|</span> Filmproduktion<br>Uferweg 12<br>12043 Berlin</div>
    <ul class="contact bullet-list" style="left:72px"><li>(01 70) 5 28 41 06</li><li>berger@lichtkante.example</li><li>www.lichtkante.example</li></ul>
  </article>

  <article class="card card-front" aria-label="Visitenkarte Vorderseite">
    <div class="wordmark">Lichtkante</div>
  </article>

</body>
</html>
```